Business card, FB Profile Cover Page & Postcard Flyer

For the Business card, we would like the following contents/texts.
Suggestions (not required) for the placements of contents:
The front
Company name with tagline (where love happens)
Full name
Title (Chief Executive or Managing Director)
Mobile number
Email address style: first.lastname@velmoranth.com
And the back:
Company logo and full web address www.velmoranth.com
Company UK address – Velmoranth (Europe) Limited, Third Floor,
418 Pelham Crescent, London
N4K 7QP (commas are not required)
In small or subtle print “registered in England No. 47xxxx”
Registered office: 9 Audley Byre Court, London, S52 6JD registered in England. Company no.
The look and fill should be simple, elegant, classy and luxurious.

FaceBook Cover Image

We would like a design of our FaceBook profile cover.
For the Cover Image – we would like you to use your initiative and creativity to ensure the style, look and feel are consistent with the company logo. We would like to see the company logo, and some texts with a background image, preferably with some illustration, however, an original work based on loyalty free photos or images can be acceptable.
We would like a cover text to appear on the cover image, “Love happens 2160 truths later, in less than 90 seconds. How can we make love happen for you? Visit www.velmoranth.com”. Email info@velmoranth.com

Postcard flyer

Like the Facebook Cover Image, we would like you to use your initiative and creativity to ensure the style, look and feel are consistent with the logo you created for the company. We welcome illustration or original work based on loyalty free photos or images. Text/content wise we would like,
Company web address, logo, email (info@velmoranth.com)
“Love happens 2,160 truths later, in less than 90 seconds. May we make love happen for you? Visit www.velmoranth.com or email us now info@velmoranth.com"

```html
<!DOCTYPE html>
<html lang="en">
<head>
<meta charset="utf-8">
<title>Velmoranth – Brand Collateral</title>
<link rel="stylesheet" href="https://fonts.googleapis.com/css2?family=Open+Sans:wght@300;400;600&display=swap">
<style>
  :root {
    --board: #3a2116;
    --purple: #3f0a5c;
    --pink: #e04bb4;
    --yellow: #f2c230;
    --white: #ffffff;
    --label: #f4ece6;
  }
  * { box-sizing: border-box; margin: 0; padding: 0; }
  html, body { width: 1200px; height: 1000px; overflow: hidden; }
  body {
    position: relative;
    background: var(--board);
    font-family: "Open Sans", sans-serif;
    font-weight: 300;
    color: var(--white);
  }
  .piece { position: absolute; overflow: hidden; box-shadow: 0 6px 18px rgba(0,0,0,.45); }
  .abs { position: absolute; white-space: nowrap; line-height: 1; }
  .pattern { position: absolute; inset: 0; width: 100%; height: 100%; }

  .board-label { position: absolute; color: var(--label); font-weight: 300; line-height: 1.3; }
  .board-label--large { font-size: 44px; }
  .board-label--small { font-size: 28px; }

  .brand-mark { position: absolute; background: var(--pink); }
  .brand-name { font-weight: 400; letter-spacing: .5px; }
  .pink { color: var(--pink); }
  .yellow { color: var(--yellow); }

  /* Facebook cover */
  .fb-cover { left: 68px; top: 30px; width: 794px; height: 292px; background: var(--purple); }
  .fb-profile {
    position: absolute; left: 86px; top: 224px; width: 159px; height: 158px;
    background: var(--purple); border: 4px solid var(--white);
    box-shadow: 0 6px 18px rgba(0,0,0,.45);
  }

  /* Postcard */
  .postcard { left: 333px; top: 344px; width: 525px; height: 350px; background: var(--purple); }

  /* Business card */
  .card-front { left: 165px; top: 715px; width: 465px; height: 265px; background: var(--purple); }
  .card-back { left: 656px; top: 717px; width: 461px; height: 263px; background: var(--white); color: var(--purple); }
  .band { position: absolute; }
  .band--white { background: var(--white); }
  .band--purple { background: var(--purple); }
</style>
</head>
<body>

  <p class="board-label board-label--large" style="left:900px;top:100px;">Facebook<br>Design</p>
  <p class="board-label board-label--large" style="left:900px;top:338px;">Postcard<br>Design</p>
  <p class="board-label board-label--small" style="left:931px;top:668px;">Business Card</p>

  <!-- Facebook cover -->
  <section class="piece fb-cover">
    <svg class="pattern" viewBox="0 0 794 292" role="img" aria-label="Scattered pink and white outline hearts framing the cover">
      <defs>
        <radialGradient id="fbHeartsA" cx="0" cy="0" r="1">
          <stop offset="0" stop-color="#b23a9c" stop-opacity=".85"/>
          <stop offset="1" stop-color="#3f0a5c" stop-opacity="0"/>
        </radialGradient>
        <radialGradient id="fbHeartsB" cx="1" cy="1" r="1">
          <stop offset="0" stop-color="#c8429f" stop-opacity=".9"/>
          <stop offset="1" stop-color="#3f0a5c" stop-opacity="0"/>
        </radialGradient>
      </defs>
      <rect x="0" y="0" width="300" height="230" fill="url(#fbHeartsA)"/>
      <rect x="230" y="0" width="564" height="292" fill="url(#fbHeartsB)"/>
    </svg>
    <span class="brand-mark" style="left:330px;top:62px;width:34px;height:34px;"></span>
    <span class="abs brand-name" style="left:394px;top:60px;font-size:34px;">VELMORANTH</span>
    <span class="abs pink" style="left:306px;top:122px;font-size:13px;">Love <span style="color:var(--white)">happens</span></span>
    <span class="abs" style="left:306px;top:138px;font-size:13px;"><span class="yellow" style="font-size:20px;">2160 truths</span> <span style="font-size:20px;">later</span>, in less than <span class="yellow">90 seconds.</span></span>
    <span class="abs" style="left:357px;top:167px;font-size:12px;">How can we make <span class="pink">love</span> happen for you?</span>
    <span class="abs" style="left:359px;top:182px;font-size:21px;">Visit <span class="yellow">www.velmoranth.com</span></span>
  </section>
  <div class="fb-profile">
    <span class="brand-mark" style="left:60px;top:60px;width:31px;height:31px;"></span>
  </div>

  <!-- Postcard -->
  <section class="piece postcard">
    <svg class="pattern" viewBox="0 0 525 350" role="img" aria-label="Cascade of pink and white outline hearts along the left and bottom edges">
      <defs>
        <linearGradient id="pcHeartsL" x1="0" y1="0" x2="1" y2="0">
          <stop offset="0" stop-color="#b8409f" stop-opacity=".85"/>
          <stop offset="1" stop-color="#3f0a5c" stop-opacity="0"/>
        </linearGradient>
        <linearGradient id="pcHeartsB" x1="0" y1="1" x2="0" y2="0">
          <stop offset="0" stop-color="#c8429f" stop-opacity=".9"/>
          <stop offset="1" stop-color="#3f0a5c" stop-opacity="0"/>
        </linearGradient>
      </defs>
      <rect x="0" y="0" width="220" height="350" fill="url(#pcHeartsL)"/>
      <rect x="0" y="230" width="525" height="120" fill="url(#pcHeartsB)"/>
    </svg>
    <span class="brand-mark" style="left:222px;top:48px;width:30px;height:30px;"></span>
    <span class="abs brand-name" style="left:264px;top:49px;font-size:27px;">VELMORANTH</span>
    <span class="abs pink" style="left:222px;top:114px;font-size:14px;">Love <span style="color:var(--white)">happens</span></span>
    <span class="abs yellow" style="left:222px;top:132px;font-size:21px;">2160 truths <span style="color:var(--white)">later,</span></span>
    <span class="abs" style="left:296px;top:158px;font-size:15px;">in less than <span class="yellow">90 seconds.</span></span>
    <span class="abs" style="left:222px;top:228px;font-size:11px;">How can we make <span class="pink">love</span> happen for you?</span>
    <span class="abs" style="left:222px;top:243px;font-size:17px;">Visit <span class="yellow">www.velmoranth.com</span></span>
  </section>

  <!-- Business card front -->
  <section class="piece card-front">
    <span class="band band--white" style="left:0;top:115px;width:15px;height:40px;"></span>
    <span class="band band--white" style="left:293px;top:115px;width:172px;height:40px;"></span>
    <span class="brand-mark" style="left:34px;top:120px;width:26px;height:26px;"></span>
    <span class="abs brand-name" style="left:72px;top:122px;font-size:22px;">VELMORANTH</span>
    <span class="abs" style="left:34px;top:181px;font-size:15px;">Daniel Harrow <span class="yellow" style="font-size:8px;letter-spacing:.5px;">MANAGING DIRECTOR</span></span>
    <span class="abs" style="left:34px;top:203px;font-size:11px;"><span class="yellow">m</span>&nbsp; 020 7946 0321</span>
    <span class="abs" style="left:34px;top:219px;font-size:11px;"><span class="yellow">e</span>&nbsp; danielharrow@velmoranth.com</span>
  </section>

  <!-- Business card back -->
  <section class="piece card-back">
    <span class="band band--purple" style="left:0;top:113px;width:11px;height:42px;"></span>
    <span class="band band--purple" style="left:289px;top:113px;width:172px;height:42px;"></span>
    <span class="abs" style="left:289px;top:92px;font-size:14px;font-weight:400;">www.velmoranth.com</span>
    <span class="brand-mark" style="left:33px;top:120px;width:28px;height:28px;"></span>
    <span class="abs brand-name" style="left:73px;top:121px;font-size:23px;">VELMORANTH</span>
    <span class="abs" style="left:33px;top:175px;font-size:12px;">Velmoranth (Europe) Limited</span>
    <span class="abs" style="left:33px;top:193px;font-size:12px;">Third Floor&nbsp; 418 Pelham Crescent</span>
    <span class="abs" style="left:33px;top:211px;font-size:12px;">London N4K 7QP</span>
    <span class="abs" style="left:33px;top:230px;font-size:7px;">Registered in England. Comp No.47xxxx</span>
  </section>

</body>
</html>
```